brisvole For High end Builder/developer construction

We will be a residential building company focused on a meticulous approach to high end quality builds with a design collaborative approach with all our clients to push the boundaries on new forms, products and bespoke architectural designs.

We want to be known to thrives upon collaboration with architects, designers and our clients to help them transform big ideas into inspiring spaces. We run every part of the building process, from planning through to construction and completion, is detail-focused and seamlessly managed.

Target Market(s)

High end

Font styles to use
Other font styles liked:
• Gotham Light

Colors

Designer to choose only greyscale colors for use in the design.

Requirements
Must have
• Bold headed incorporating sharp features for the logo to standout in mostly black to ensure the logo pops

```html
<!DOCTYPE html>
<html lang="en">
<head>
<meta charset="utf-8">
<title>Norvane Build Letterhead</title>
<link rel="stylesheet" href="https://fonts.googleapis.com/css2?family=Lato:wght@400&family=Encode+Sans+Condensed:wght@300;400&display=swap">
<style>
  :root {
    --backdrop: #d6d6d6;
    --paper: #ffffff;
    --ink: #111111;
    --text: #4f4f4f;
    --contact: #444444;
    --accent: #2e2e2e;
    --icon: #5a5a5a;
    --rule: #9a9a9a;
    --accent-soft: #e4e4e4;
  }
  * { box-sizing: border-box; margin: 0; padding: 0; }
  html, body {
    width: 1056px;
    height: 1200px;
    overflow: hidden;
    background: var(--backdrop);
  }
  .letterhead {
    position: absolute;
    left: 117px;
    top: 20px;
    width: 821px;
    height: 1160px;
    background: var(--paper);
  }
  .brand {
    position: absolute;
    left: 50px;
    top: 150px;
    display: flex;
    align-items: center;
    gap: 10px;
    font-family: "Lato", sans-serif;
    font-weight: 400;
    font-size: 17px;
    letter-spacing: 3px;
    color: var(--ink);
    text-transform: uppercase;
  }
  .brand-square {
    width: 12px;
    height: 12px;
    background: var(--ink);
  }
  .contact {
    position: absolute;
    right: 52px;
    top: 68px;
    font-family: "Lato", sans-serif;
    font-size: 15.5px;
    color: var(--contact);
    text-align: right;
  }
  .address { line-height: 19px; margin-bottom: 10px; padding-right: 5px; }
  .contact-line {
    display: flex;
    justify-content: flex-end;
    align-items: center;
    gap: 13px;
    height: 22px;
  }
  .contact-line svg { width: 15px; height: 15px; }
  .header-rule {
    position: absolute;
    left: 50px;
    width: 719px;
    top: 197px;
    height: 1px;
    background: var(--rule);
  }
  .body-copy {
    position: absolute;
    left: 79px;
    width: 667px;
    top: 355px;
    font-family: "Encode Sans Condensed", sans-serif;
    font-weight: 300;
    font-size: 19.6px;
    line-height: 28.5px;
    color: var(--text);
  }
  .body-copy p { text-align: justify; margin-bottom: 28.5px; }
  .body-copy .salutation { text-align: left; margin-bottom: 25px; }
  .closing {
    position: absolute;
    left: 79px;
    top: 937px;
    font-family: "Encode Sans Condensed", sans-serif;
    font-weight: 300;
    font-size: 19.6px;
    color: var(--text);
  }
  .signature {
    position: absolute;
    left: 76px;
    top: 977px;
    width: 66px;
    height: 40px;
    background: var(--accent-soft);
  }
  .footer-band {
    position: absolute;
    left: 0;
    bottom: 0;
    width: 100%;
    height: 13px;
    background: var(--accent);
  }
</style>
</head>
<body>
  <main class="letterhead">
    <div class="brand"><span class="brand-square"></span>Norvane Build</div>

    <div class="contact">
      <div class="address">1234 First Line Address<br>5678 Second Line Address</div>
      <div class="contact-line">1234567890
        <svg viewBox="0 0 16 16" aria-hidden="true"><path d="M4 1.5 6 5 4.6 6.4c.8 1.9 2.2 3.3 4.1 4.1L10 9l3.5 2-.8 2.6C6.5 13.6 2.4 9.5 1.5 3.3Z" fill="none" stroke="#5a5a5a" stroke-width="1.4" stroke-linejoin="round"/><path d="M9.5 2.5a4 4 0 0 1 4 4M9.5 0.8a5.7 5.7 0 0 1 5.7 5.7" fill="none" stroke="#5a5a5a" stroke-width="1.1"/></svg>
      </div>
      <div class="contact-line">info@yourmail.com
        <svg viewBox="0 0 16 16" aria-hidden="true"><rect x="1" y="3" width="14" height="10" fill="#5a5a5a"/><path d="M1 3 8 9l7-6M1 13l5-5M15 13l-5-5" fill="none" stroke="#fff" stroke-width="1"/></svg>
      </div>
      <div class="contact-line">www.yourwebsite.com
        <svg viewBox="0 0 16 16" aria-hidden="true"><g fill="none" stroke="#5a5a5a" stroke-width="1"><circle cx="8" cy="8" r="6.5"/><ellipse cx="8" cy="8" rx="3" ry="6.5"/><path d="M1.5 8h13M2.5 4.8h11M2.5 11.2h11"/></g></svg>
      </div>
    </div>

    <div class="header-rule"></div>

    <section class="body-copy">
      <p class="salutation">Dear Sir/Mam,</p>
      <p>Contrary to popular belief, Lorem Ipsum is not simply random text. It has roots in a piece of classical Latin literature from 45 BC, making it over 2000 years old. Daniel Okafor, a Latin professor at Ashgrove College in Virginia, looked up one of the more obscure Latin words, consectetur.</p>
      <p>Lorem Ipsum comes from sections 1.10.32 and 1.10.33 of "de Finibus Bonorum et Malorum" (The Extremes of Good and Evil) by Varellus, written in 45 BC. This book is a treatise on the theory of ethics, very popular during the Renaissance. The first line of Lorem Ipsum.</p>
      <p>The standard chunk of Lorem Ipsum used since the 1500s is reproduced below for those interested. Sections 1.10.32 and 1.10.33 from "de Finibus Bonorum et Malorum" by Varellus are also reproduced in their exact original.</p>
      <p>The standard chunk of Lorem Ipsum used since the 1500s is reproduced below for those interested.</p>
    </section>

    <div class="closing">Best Regards</div>
    <div class="signature" role="img" aria-label="Handwritten signature of Harlow"></div>

    <div class="footer-band"></div>
  </main>
</body>
</html>
```